Old Shanghai birthday party (1920s - 1930s)

I need an invitation for a joint birthday party; basically we will celebrate a couple: she's turning 40 and he's turning 45). The idea of the venue decoration is very sophisticate, with red lanterns, old style painted paper umbrellas and fans, check it out for your reference
https://www.tackboardly.com/rennavost/jazz-harbour/
Here the details to write down:
Marta and Dennis
are turning 85 !
Come celebrate with us!
Saturday, September 10th, 2016 at 8 pm
Quillberry
7C, 19 Tai Lok Fung Road, Aberdeen, Hong Kong
If you can come, please RSVP to Marta Felcote by August 20th
at (852) 471 26508
Dress code: Old Shanghai

Target Market(s)
Adults around 40 years old (The couple is from Australia)

```html
<!DOCTYPE html>
<html lang="en">
<head>
<meta charset="utf-8">
<title>Marta &amp; Dennis are turning 85 – Invitation</title>
<link href="https://fonts.googleapis.com/css2?family=Archivo+Black&family=Francois+One&family=Oswald:wght@500;600&display=swap" rel="stylesheet">
<style>
  :root {
    --lantern-red: #c4121a;
    --deep-red: #3a0406;
    --wine: #6e0a0e;
    --title-red: #e02a1f;
    --rsvp-red: #e3261d;
    --white: #ffffff;
    --ink: #0b0606;
    --poster-grey: #4a4442;
    --poster-dark: #241f1e;
    --gold: #e6b45a;
    --amber: #8a4a16;
  }
  html, body {
    margin: 0;
    padding: 0;
    width: 846px;
    height: 1200px;
    overflow: hidden;
    background: var(--deep-red);
  }
  .invitation {
    position: relative;
    width: 846px;
    height: 1200px;
    overflow: hidden;
    font-family: "Oswald", "Arial Narrow", sans-serif;
  }
  .venue-photo {
    position: absolute;
    inset: 0;
    background:
      radial-gradient(ellipse 140px 120px at 330px 130px, rgba(230,40,40,.85), transparent 70%),
      radial-gradient(ellipse 150px 170px at 735px 190px, rgba(220,30,35,.9), transparent 72%),
      radial-gradient(ellipse 120px 110px at 560px 300px, rgba(200,25,30,.8), transparent 70%),
      radial-gradient(ellipse 90px 100px at 40px 460px, rgba(190,20,25,.8), transparent 70%),
      radial-gradient(ellipse 220px 140px at 170px 860px, rgba(200,40,40,.55), transparent 70%),
      linear-gradient(180deg, #4b0a0c 0%, var(--wine) 30%, #4a0608 60%, #2c0204 100%);
  }
  .poster-photo {
    position: absolute;
    left: 346px;
    top: 555px;
    width: 500px;
    height: 645px;
    background: linear-gradient(180deg, var(--poster-grey) 0%, #3b3533 45%, var(--poster-dark) 100%);
    opacity: .93;
  }
  .headline, .age {
    position: absolute;
    left: 0;
    top: 0;
  }
  .headline text {
    font-family: "Francois One", "Arial Black", sans-serif;
    font-size: 64px;
    fill: var(--title-red);
    stroke: var(--white);
    stroke-width: 7px;
    paint-order: stroke;
    stroke-linejoin: round;
  }
  .age text {
    font-family: "Archivo Black", "Arial Black", sans-serif;
    font-size: 440px;
  }
  .age .age-shadow { fill: var(--ink); }
  .age .age-fill {
    fill: url(#ageFill);
    stroke: var(--white);
    stroke-width: 7px;
    paint-order: stroke;
  }
  .details {
    position: absolute;
    left: 346px;
    top: 742px;
    width: 440px;
    text-align: center;
    color: var(--white);
    font-weight: 500;
    font-size: 22px;
    line-height: 31px;
    letter-spacing: .3px;
  }
  .details p { margin: 0; }
  .details .venue-name { margin-top: 2px; }
  .rsvp {
    position: absolute;
    left: 346px;
    top: 978px;
    width: 440px;
    text-align: center;
    color: var(--rsvp-red);
    font-weight: 500;
    font-size: 18px;
    line-height: 32px;
    letter-spacing: .3px;
  }
  .rsvp p { margin: 0; }
  .rsvp .dress-code { margin-top: 30px; }
</style>
</head>
<body>
<main class="invitation">
  <div class="venue-photo" role="img" aria-label="Restaurant dining room decorated with hanging red paper lanterns and red table flowers"></div>
  <div class="poster-photo" role="img" aria-label="Vintage Old Shanghai poster of a woman in a qipao with Chinese lettering"></div>

  <svg class="headline" width="846" height="260" viewBox="0 0 846 260" aria-label="Marta &amp; Dennis are turning">
    <text x="430" y="152" text-anchor="middle">Marta &amp; Dennis</text>
    <text x="430" y="232" text-anchor="middle">are turning</text>
  </svg>

  <svg class="age" width="846" height="660" viewBox="0 0 846 660" aria-label="85!">
    <defs>
      <linearGradient id="ageFill" x1="0" y1="0" x2="0" y2="1">
        <stop offset="0" stop-color="var(--gold)"/>
        <stop offset=".45" stop-color="var(--amber)"/>
        <stop offset="1" stop-color="#5a1a0c"/>
      </linearGradient>
    </defs>
    <g class="age-shadow">
      <text x="80" y="636" textLength="230" lengthAdjust="spacingAndGlyphs">8</text>
      <text x="310" y="636" textLength="200" lengthAdjust="spacingAndGlyphs">5</text>
      <text x="655" y="636" textLength="90" lengthAdjust="spacingAndGlyphs">!</text>
    </g>
    <g class="age-fill">
      <text x="92" y="628" textLength="230" lengthAdjust="spacingAndGlyphs">8</text>
      <text x="322" y="628" textLength="200" lengthAdjust="spacingAndGlyphs">5</text>
      <text x="667" y="628" textLength="90" lengthAdjust="spacingAndGlyphs">!</text>
    </g>
  </svg>

  <section class="details">
    <p>Saturday, September 10th, 2016</p>
    <p>at 8 pm</p>
    <p class="venue-name">Quillberry</p>
    <p>7C, 19 Tai Lok Fung Road,</p>
    <p>Aberdeen, Hong Kong</p>
  </section>

  <section class="rsvp">
    <p>If you can come, please RSVP to</p>
    <p>Marta Felcote by August 20th</p>
    <p>at (852) 471 26508</p>
    <p class="dress-code">Dress Code : Old Shanghai</p>
  </section>
</main>
</body>
</html>
```